Redesign of Business Card to look more professional and stand out

Business card design. You can lean more about our company by going to dkrfabworks.example. Raised letters would be nice. Company name & Address
DK&R
418 Wendlow Ridge Drive, Suite 340
Calder Falls, AL 35999

You can use my name and title: Glenn Harwick
Business Development Manager

Target Market(s)

Heavy Industrial market, i.e. utilities, chemical plants, paper mills, construction companies

Industry/Entity Type

Construction

Contact Information for Business Card

We provide Project Management & Project Support Services

Font styles to use
Serif

Requirements
Must have
• Company name & Address
• DK&R
• 418 Wendlow Ridge Drive, Suite 340
• Calder Falls, AL 35999
Nice to have
• ideas for the back of the card
Should not have
• no crazy colors. needs to look professional and standout.

```html
<!DOCTYPE html>
<html lang="en">
<head>
<meta charset="utf-8">
<title>DK&amp;R Business Card</title>
<link href="https://fonts.googleapis.com/css2?family=PT+Sans:ital,wght@0,400;0,700;1,700&display=swap" rel="stylesheet">
<style>
  :root {
    --backdrop: #9b9c9e;
    --card-paper: #eeeff1;
    --navy: #1b2d5a;
    --navy-deep: #16264e;
    --slate: #6e7490;
    --ink: #4a4d55;
    --rule: #9ea3b3;
    --band-edge: #8d93a6;
    --white: #ffffff;
  }
  * { margin: 0; padding: 0; box-sizing: border-box; }
  html, body { width: 1105px; height: 1200px; overflow: hidden; }
  body {
    background: var(--backdrop);
    font-family: "PT Sans", Arial, sans-serif;
    position: relative;
  }
  .card {
    position: absolute;
    left: 182px;
    width: 747px;
    height: 427px;
    overflow: hidden;
  }
  .card-front { top: 119px; background: var(--card-paper); }
  .card-back { top: 637px; background: var(--navy-deep); }

  .brand-name {
    position: absolute;
    font-weight: 700;
    letter-spacing: -1px;
    line-height: 1;
  }
  .card-front .brand-name {
    left: 56px; top: 142px;
    font-size: 110px;
    color: var(--navy);
  }
  .divider {
    position: absolute;
    left: 369px; top: 61px;
    width: 1px; height: 270px;
    background: var(--rule);
  }
  .details { position: absolute; left: 393px; top: 60px; }
  .person-name { font-size: 26px; font-weight: 700; color: var(--navy); line-height: 1.2; }
  .person-title { font-size: 19px; color: var(--slate); line-height: 1.2; }
  .address { margin-top: 14px; font-size: 19px; color: var(--ink); line-height: 27px; font-style: normal; }
  .contacts { list-style: none; margin-top: 10px; }
  .contacts li {
    display: flex; align-items: center;
    font-size: 19px; color: var(--ink);
    height: 28px;
  }
  .contacts svg { width: 16px; height: 16px; margin-right: 8px; margin-left: 5px; fill: var(--navy); flex: none; }

  .footer-band { position: absolute; left: 0; bottom: 0; width: 747px; height: 80px; }
  .tagline {
    position: absolute; left: 0; right: 0; bottom: 8px;
    text-align: center;
    font-size: 19px; font-weight: 700; font-style: italic;
    color: var(--white);
  }

  .card-back .brand-name {
    right: 38px; top: 288px;
    font-size: 86px;
    color: var(--white);
  }
  .back-url {
    position: absolute; right: 38px; top: 376px;
    font-size: 19px; color: var(--white);
  }
</style>
</head>
<body>
  <section class="card card-front">
    <div class="brand-name">DK&amp;R</div>
    <div class="divider"></div>
    <div class="details">
      <div class="person-name">Glenn Harwick</div>
      <div class="person-title">Business Development Manager</div>
      <address class="address">418 Wendlow Ridge Drive<br>Suite 340<br>Calder Falls, AL 35999</address>
      <ul class="contacts">
        <li><svg viewBox="0 0 16 16"><path d="M3.2 1l2.6 3-1.5 2a9 9 0 0 0 5.7 5.7l2-1.5 3 2.6-1.5 2.2C7 15.5.5 9 1 2.5z"/></svg>205-555-0148</li>
        <li><svg viewBox="0 0 16 16"><path d="M4 0h8a1 1 0 0 1 1 1v14a1 1 0 0 1-1 1H4a1 1 0 0 1-1-1V1a1 1 0 0 1 1-1zm1 2v10h6V2zm3 11a1 1 0 1 0 0 2 1 1 0 0 0 0-2z"/></svg>205-555-0172</li>
        <li><svg viewBox="0 0 16 16"><path d="M0 3h16v10H0zm1.5 1.2V5l6.5 4 6.5-4v-.8z"/></svg>glenn@dkrfabworks.example</li>
        <li><svg viewBox="0 0 16 16"><circle cx="8" cy="8" r="7.5"/><path d="M5 3c2 1 1 3 3 4s0 3 2 4M10 2c0 2 3 2 4 4" stroke="#eeeff1" stroke-width="1.3" fill="none"/></svg>www.dkrfabworks.example</li>
      </ul>
    </div>
    <svg class="footer-band" viewBox="0 0 747 80" preserveAspectRatio="none">
      <path d="M0 38 Q373 -4 747 38 L747 80 L0 80 Z" fill="var(--band-edge)"/>
      <path d="M0 45 Q373 4 747 45 L747 80 L0 80 Z" fill="var(--navy)"/>
    </svg>
    <div class="tagline">We provide Project Management &amp; Project Support Services</div>
  </section>

  <section class="card card-back">
    <div class="brand-name">DK&amp;R</div>
    <div class="back-url">www.dkrfabworks.example</div>
  </section>
</body>
</html>
```